Wordpress website for voluntary transgender support online

We need a website as an information support for transgender people and their friends and families. We are a self funded voluntary support group reaching out to educate all in need.
Fairly basic site. Tabs for 3 of us to put bios, professional resources and contacts, news, general information, our contact info, entertainment.
Our logo is attached and we'd love the use of clouds and the colour lilac. We wish to look professional but approachable and personable.

Target Market(s)

Transgender people,mr heir families and friends and general public.

Industry/Entity Type

Group

Requirements
Must have
• Willow 4 logo.
• Tabs for: about us, contacts, news, bios x3, suggestions, professional resources, entertainment, personal resources, general information.
• We are hoping to set up in Wordpress so that we can then manage the page and update in the future.
• Coding will be required.
Nice to have
• Any suggestions.

```html
<!DOCTYPE html>
<html lang="en">
<head>
<meta charset="utf-8">
<title>Willow 4 – Transgender Support</title>
<link href="https://fonts.googleapis.com/css2?family=Open+Sans:wght@300;400;600;700&family=Great+Vibes&display=swap" rel="stylesheet">
<style>
:root{
  --purple:#6c2b88;
  --purple-dark:#4f1d66;
  --lilac:#ede2f2;
  --lilac-mid:#d7c3e2;
  --text:#555;
  --heading:#5d2a76;
  --muted:#999;
  --white:#fff;
  --line:#e4dbe8;
}
*{box-sizing:border-box;margin:0;padding:0}
html,body{width:1200px;height:2276px;overflow:hidden}
body{font-family:"Open Sans",Arial,sans-serif;color:var(--text);background:linear-gradient(#fff 0,#fff 900px,var(--lilac) 1250px,#fff 1700px,var(--lilac) 2150px);position:relative}

.site-header{height:144px;display:flex;align-items:center;justify-content:space-between;padding:0 60px;background:#fff}
.brand{display:flex;align-items:center;gap:14px;font-size:44px;font-weight:300;color:var(--purple)}
.brand-dot{width:22px;height:22px;border-radius:50%;background:var(--purple)}
.main-nav{display:flex;gap:6px}
.main-nav a{font-size:15px;color:#777;text-decoration:none;padding:10px 16px;border:1px solid transparent;border-radius:4px}
.main-nav a.active{border-color:#ccc;color:#333}

.hero{position:relative;height:560px;overflow:hidden}
.hero-photo{position:absolute;inset:0;background:radial-gradient(circle at 40% 40%,#c9a98a 0,#8a6b54 35%,#4a3a33 70%,#2f2824 100%)}
.hero-wave{position:absolute;left:0;bottom:0;width:1200px;height:140px}
.hero-caption{position:absolute;right:90px;top:300px;font-family:"Great Vibes",cursive;font-size:46px;line-height:1.05;color:#fff;text-align:right}
.hero-arrow{position:absolute;top:260px;width:30px;height:40px}
.hero-arrow.left{left:18px}.hero-arrow.right{right:18px}

.section-title{text-align:center;font-weight:300;font-size:40px;color:var(--heading)}
.title-rule{width:90px;height:2px;background:var(--lilac-mid);margin:16px auto 0}

.welcome{padding:50px 110px 0;text-align:center}
.welcome .lead{margin-top:28px;font-size:15px;font-weight:600;color:#444;line-height:1.6}
.welcome p{margin-top:20px;font-size:13px;line-height:1.7;color:var(--muted)}

.mission{margin-top:70px}
.mission-list{display:flex;justify-content:space-between;padding:0 110px;margin-top:44px}
.mission-item{width:176px;text-align:center;font-size:12px;line-height:1.5;color:#777}
.mission-item svg{width:44px;height:44px;margin-bottom:14px}

.news{margin-top:100px;position:relative}
.news-row{display:flex;gap:20px;padding:0 120px;margin-top:40px}
.news-card{width:225px}
.news-thumb{height:200px}
.news-card h3{font-size:12px;font-weight:600;color:var(--purple);margin-top:12px}
.news-card time{font-size:11px;color:var(--muted)}
.news-arrow{position:absolute;top:230px;width:20px;height:30px}
.news-arrow.left{left:90px}.news-arrow.right{right:90px}

.testimonial{margin:70px 120px 0;height:272px;display:flex;background:#fff;border:1px solid var(--line)}
.testimonial-body{flex:1;padding:46px 50px;position:relative}
.quote-mark{position:absolute;font-size:60px;color:var(--purple);font-weight:700;line-height:1}
.quote-mark.open{left:20px;top:30px}.quote-mark.close{right:20px;top:120px}
.testimonial-body p{font-size:14px;line-height:1.75;color:#777;font-style:italic;padding-left:20px}
.testimonial-body cite{display:block;margin-top:22px;padding-left:20px;font-style:normal;font-weight:600;color:var(--purple);font-size:15px}
.testimonial-photo{width:330px;background:linear-gradient(120deg,#d9d2d5,#bfb3b6 50%,#e8e1e3)}

.contact{margin-top:120px;text-align:center}
.contact-line{display:flex;justify-content:center;gap:40px;margin-top:30px;font-size:14px;color:#666}
.contact-line span{display:flex;align-items:center;gap:8px}
.contact-line svg{width:16px;height:16px}

.site-footer{position:absolute;left:0;bottom:0;width:1200px;height:116px;background:var(--purple);color:#e6d8ee;padding:28px 60px;display:flex;justify-content:space-between;align-items:center}
.footer-nav{display:flex;gap:10px;font-size:13px}
.footer-nav a{color:#f0e6f5;text-decoration:none}
.copyright{font-size:12px;margin-top:12px;color:#cdb6da}
.social{display:flex;gap:10px}
.social span{width:34px;height:34px;border-radius:50%;background:#fff;opacity:.9}
</style>
</head>
<body>

<header class="site-header">
  <div class="brand"><span class="brand-dot"></span>Willow 4</div>
  <nav class="main-nav">
    <a class="active" href="#">Home</a><a href="#">About us</a><a href="#">Bios</a><a href="#">News</a><a href="#">Suggestions</a><a href="#">Resources</a><a href="#">Contact us</a>
  </nav>
</header>

<section class="hero">
  <div class="hero-photo" role="img" aria-label="Portrait of a woman with long blonde hair"></div>
  <div class="hero-caption">Phasellus nisl est<br>condimentum vitae faucibus</div>
  <svg class="hero-arrow left" viewBox="0 0 30 40"><path d="M22 4 6 20l16 16" fill="none" stroke="#fff" stroke-width="4"/></svg>
  <svg class="hero-arrow right" viewBox="0 0 30 40"><path d="M8 4l16 16L8 36" fill="none" stroke="#fff" stroke-width="4"/></svg>
  <svg class="hero-wave" viewBox="0 0 1200 140" preserveAspectRatio="none">
    <path d="M0 40 C300 140 700 140 1200 20 L1200 140 L0 140Z" fill="#7a3a99"/>
    <path d="M0 70 C320 150 720 150 1200 50 L1200 140 L0 140Z" fill="#fff"/>
  </svg>
</section>

<section class="welcome">
  <h2 class="section-title">Welcome to Willow 4</h2>
  <div class="title-rule"></div>
  <p class="lead">Willow 4 is a Peer Transgender and crossdressing support group committed to providing support and understanding to the transgender, cross dresser and gender diverse group including their partners, family and friends.</p>
  <p>We know if you are new to this world, people with similar experiences and a source of help make such a difference. Our peer support group welcomes everyone who is curious about gender identity, whether you are just starting out or have been exploring for years. We meet online and in person, share honest stories, and point you to kind professionals when you need more.</p>
</section>

<section class="mission">
  <h2 class="section-title">Our Mission</h2>
  <div class="title-rule"></div>
  <div class="mission-list">
    <div class="mission-item"><svg viewBox="0 0 44 44"><circle cx="15" cy="14" r="7" fill="#6c2b88"/><circle cx="30" cy="16" r="6" fill="#6c2b88"/><path d="M2 40c0-10 6-16 13-16s13 6 13 16zM24 40c1-8 4-13 8-13s10 5 10 13z" fill="#6c2b88"/></svg>To provide support and services to the transgender community, their family and friends</div>
    <div class="mission-item"><svg viewBox="0 0 44 44"><path d="M22 38 6 22a9 9 0 0 1 16-10 9 9 0 0 1 16 10z" fill="#6c2b88"/></svg>To empower individuals with support and information to allow them to accept their selves and be proud</div>
    <div class="mission-item"><svg viewBox="0 0 44 44"><path d="M10 4h18l8 8v28H10z" fill="#6c2b88"/><path d="M15 20h16M15 26h16M15 32h12" stroke="#fff" stroke-width="2"/></svg>To provide information and contacts already for gender diverse family members</div>
    <div class="mission-item"><svg viewBox="0 0 44 44"><path d="M22 8 2 18l20 10 20-10z" fill="#6c2b88"/><path d="M10 23v9c6 5 18 5 24 0v-9l-12 6z" fill="#6c2b88"/></svg>To provide education and awareness within the broader community</div>
    <div class="mission-item"><svg viewBox="0 0 44 44"><circle cx="22" cy="22" r="18" fill="#6c2b88"/><path d="M22 22V4a18 18 0 0 1 18 18z" fill="#c9a9d9"/></svg>To hopefully lessen the intolerance and unacceptable attitudes within our community</div>
  </div>
</section>

<section class="news">
  <h2 class="section-title">Recent News</h2>
  <div class="title-rule"></div>
  <svg class="news-arrow left" viewBox="0 0 20 30"><path d="M15 3 4 15l11 12" fill="none" stroke="#aaa" stroke-width="3"/></svg>
  <svg class="news-arrow right" viewBox="0 0 20 30"><path d="M5 3l11 12L5 27" fill="none" stroke="#aaa" stroke-width="3"/></svg>
  <div class="news-row">
    <article class="news-card"><div class="news-thumb" role="img" aria-label="Performer in a feathered costume on stage" style="background:linear-gradient(160deg,#5a7fa8,#2b3f5e)"></div><h3>Sed nisi tellus ipsum nec tellus</h3><time>July 1, 2015</time></article>
    <article class="news-card"><div class="news-thumb" role="img" aria-label="Group of friends at a community event" style="background:linear-gradient(160deg,#8a6a55,#3e3029)"></div><h3>Sed nisi tellus ipsum nec tellus</h3><time>July 1, 2015</time></article>
    <article class="news-card"><div class="news-thumb" role="img" aria-label="Couple at a pride celebration" style="background:linear-gradient(160deg,#9bb07a,#56634a)"></div><h3>Sed nisi tellus ipsum nec tellus</h3><time>July 1, 2015</time></article>
    <article class="news-card"><div class="news-thumb" role="img" aria-label="Colourful crowd at a pride parade" style="background:linear-gradient(160deg,#c46a6a,#6a4f8a)"></div><h3>Sed nisi tellus ipsum nec tellus</h3><time>July 1, 2015</time></article>
  </div>
</section>

<section class="testimonial">
  <div class="testimonial-body">
    <span class="quote-mark open">“</span>
    <p>Donec vestibulum velit sem, at laoreet massa ullamcorper sit. Donec molestie sem et tellus hendrerit lobortis. Nunc eu ligula sed ipsum pulvinar maximus et vitae enim. Proin porta fermentum ipsum, eu facilisis turpis commodo luctus.</p>
    <span class="quote-mark close">”</span>
    <cite>Marina, NY</cite>
  </div>
  <div class="testimonial-photo" role="img" aria-label="Young woman looking in a mirror"></div>
</section>

<section class="contact">
  <h2 class="section-title">Contact us</h2>
  <div class="title-rule"></div>
  <div class="contact-line">
    <span><svg viewBox="0 0 16 16"><path d="M3 1h3l1 4-2 1c1 2 3 4 5 5l1-2 4 1v3c0 1-1 2-2 2C7 15 1 9 1 3c0-1 1-2 2-2z" fill="#6c2b88"/></svg>Call us : 000 555 0142</span>
    <span><svg viewBox="0 0 16 16"><rect x="1" y="3" width="14" height="10" fill="#6c2b88"/><path d="M1 3l7 6 7-6" fill="none" stroke="#fff"/></svg>E-mail : hello@willow4.org</span>
    <span><svg viewBox="0 0 16 16"><path d="M1 2h14v9H6l-4 3v-3H1z" fill="#6c2b88"/></svg>Live Chat with us</span>
  </div>
</section>

<footer class="site-footer">
  <div>
    <nav class="footer-nav"><a href="#">Home</a>|<a href="#">About us</a>|<a href="#">Bios</a>|<a href="#">News</a>|<a href="#">Suggestions</a>|<a href="#">Resources</a>|<a href="#">Contact us</a></nav>
    <div class="copyright">Copyright © 2015 Willow 4. All rights reserved.</div>
  </div>
  <div class="social"><span></span><span></span><span></span><span></span><span></span></div>
</footer>

</body>
</html>
```